Buch-/E-Book-Cover
Zielgruppe
Wir verkaufen Trainings und vermitteln über unser Buch ein erstes vertieftes Wissen zum Thema Vermögensaufbau.
Aufgabenstellung
Es soll schlicht und schön sein, Angelehnt an Tall coin short coin, bzw. an Schau hin und bleib Klug von Bartholo Fenwick.
Wir benötigen die AI, etc Dateien und die fertigen Dateien für Velmora.de Lumora sowie Velmora.de Books (ehemals Printvale) mit fertigem Cover.
Vorgaben von Velmora.de über die Homepage. Anbei ein Beispiel (wegen Velmora.de Buchnummer etc) Abstände, Buchrücken etc.
Buch ca. 150 Seiten
https://www.velmora-beispiel.de/Gaertner-bleiben-heute-Zeichen-guten/dp/7392058164 Front und Backcover kann man sich da ansehen.
Der Buchtitel ist 'Baue Kredite und bleib frei' - - Lassen Sie uns freundschaftlich in entspannter Atmosphäre über Immobilien sprechen (der nebentitel so klein wie bei Tall Coin - Short Coin)
Rücktitel: Bitte zuerst Platzhalter.
Ich bitte um 5x8 inch, also wie DIN A 5, wir nehmen cremefarbenes Papier denke ich. Die Seitenzahl kann ich auf die Seite noch nicht sagen, wir haben aber 75 Din A4 Seiten, sprich nach Formatierung eher 160-165 Din A5. WErde ich Ihnen final nach dem Gewinn sagen.
Versuchen Sie mich mal aus dem einen Bild raus zu schneiden, und dass dann mit einem Layer über das cover zu legen.
2-3 Versionen wäre gut, mit 2-3 Bildern. Buchrücken ein kleines Bild von mir.
Seite vom Buch: Titel nochmal.

```html
<!DOCTYPE html>
<html lang="de">
<head>
<meta charset="utf-8">
<title>Baue Kredite und bleib frei – Buchumschlag</title>
<link rel="stylesheet" href="https://fonts.googleapis.com/css2?family=Open+Sans:wght@600;700;800&display=swap">
<style>
  :root {
    --violet-deep: #1a0418;
    --violet-dark: #3c0a3c;
    --violet-mid: #7a3a86;
    --violet-light: #b37bbd;
    --title-yellow: #f8d420;
    --text-white: #ffffff;
    --portrait-dark: #2f2a27;
    --portrait-light: #6b5a52;
    --font-main: "Open Sans", Arial, sans-serif;
  }
  * { margin: 0; padding: 0; box-sizing: border-box; }
  html, body { width: 1200px; height: 927px; overflow: hidden; background: var(--violet-deep); }
  .cover-wrap {
    position: relative;
    width: 1200px;
    height: 927px;
    overflow: hidden;
    font-family: var(--font-main);
    background:
      radial-gradient(ellipse 520px 420px at 860px 80px, var(--violet-light) 0%, var(--violet-mid) 35%, rgba(60,10,60,0) 80%),
      radial-gradient(ellipse 900px 700px at 700px 300px, var(--violet-dark) 0%, var(--violet-deep) 90%);
  }
  .light-rays { position: absolute; inset: 0; }
  .barcode-field {
    position: absolute;
    left: 325px; top: 753px;
    width: 223px; height: 130px;
    background: var(--text-white);
  }
  .spine-text {
    position: absolute;
    writing-mode: vertical-rl;
    font-weight: 800;
    white-space: nowrap;
    text-transform: uppercase;
  }
  .spine-author { left: 585px; top: 44px; font-size: 22px; color: var(--text-white); letter-spacing: 0.5px; }
  .spine-title { left: 587px; top: 417px; font-size: 19px; color: var(--title-yellow); letter-spacing: 0.3px; }
  .author-portrait {
    position: absolute;
    left: 578px; top: 255px;
    width: 468px; height: 640px;
    background: radial-gradient(ellipse 170px 230px at 210px 200px, var(--portrait-light) 0%, var(--portrait-dark) 75%, rgba(47,42,39,0.9) 100%);
    border-radius: 200px 200px 0 0;
  }
  .front-author {
    position: absolute;
    left: 650px; top: 40px;
    font-size: 20px; font-weight: 800;
    color: var(--text-white);
    letter-spacing: 0.4px;
    white-space: nowrap;
  }
  .title-word {
    position: absolute;
    color: var(--title-yellow);
    font-weight: 800;
    line-height: 1;
    white-space: nowrap;
    text-shadow: 2px 3px 4px rgba(20,0,20,0.55);
  }
  .title-top { left: 646px; top: 60px; font-size: 150px; letter-spacing: 14px; }
  .title-second { left: 648px; top: 196px; font-size: 95px; letter-spacing: 1px; }
  .title-joiner { left: 650px; top: 708px; font-size: 46px; font-weight: 700; }
  .title-third { left: 778px; top: 692px; font-size: 72px; letter-spacing: 2px; }
  .title-last { left: 646px; top: 740px; font-size: 162px; letter-spacing: 2px; }
  .subtitle-block {
    position: absolute;
    right: 45px; top: 358px;
    text-align: right;
    color: var(--text-white);
    text-shadow: 1px 2px 3px rgba(0,0,0,0.7);
  }
  .subtitle-kicker { font-size: 17px; font-weight: 700; letter-spacing: 1.5px; }
  .subtitle-main { font-size: 26px; font-weight: 700; letter-spacing: 1.5px; line-height: 1.55; margin-top: 8px; }
  .tagline {
    position: absolute;
    left: 880px; top: 552px;
    width: 310px;
    text-align: center;
    font-size: 16.5px; font-weight: 600;
    line-height: 1.4;
    color: var(--text-white);
    text-shadow: 1px 1px 3px rgba(0,0,0,0.8);
  }
</style>
</head>
<body>
<main class="cover-wrap">
  <svg class="light-rays" width="1200" height="927" viewBox="0 0 1200 927" aria-hidden="true">
    <defs>
      <linearGradient id="ray-fade" x1="1" y1="0" x2="0" y2="1">
        <stop offset="0" stop-color="#e2b8e8" stop-opacity="0.35"/>
        <stop offset="1" stop-color="#e2b8e8" stop-opacity="0"/>
      </linearGradient>
    </defs>
    <polygon points="850,-20 870,-20 0,210 0,120" fill="url(#ray-fade)"/>
    <polygon points="850,-20 870,-20 0,470 0,360" fill="url(#ray-fade)" opacity="0.7"/>
    <polygon points="850,-20 870,-20 380,927 250,927" fill="url(#ray-fade)" opacity="0.5"/>
    <polygon points="850,-20 870,-20 1200,320 1200,250" fill="url(#ray-fade)" opacity="0.5"/>
  </svg>

  <div class="barcode-field" aria-label="Freifläche für Buchnummer"></div>

  <div class="spine-text spine-author">Levent Morvan</div>
  <div class="spine-text spine-title">Baue Kredite und bleib frei</div>

  <div class="author-portrait" role="img" aria-label="Freigestelltes Porträtfoto des Autors im dunklen Sakko mit hellblauem Hemd und verschränkten Armen"></div>

  <div class="front-author">LEVENT MORVAN - DER IMMOBILIENADVISOR</div>

  <h1>
    <span class="title-word title-top">BAUE</span>
    <span class="title-word title-second">KREDITE</span>
    <span class="title-word title-joiner">und</span>
    <span class="title-word title-third">BLEIB</span>
    <span class="title-word title-last">FREI</span>
  </h1>

  <div class="subtitle-block">
    <div class="subtitle-kicker">GESPRÄCHE ÜBER</div>
    <div class="subtitle-main">IMMOBILIEN<br>NEBENTITEL</div>
  </div>

  <p class="tagline">Lassen Sie uns freundschaftlich in entspannter Atmosphäre über Immobilien sprechen</p>
</main>
</body>
</html>
```